Buch-/eBook-Cover für Traumatherapeutin
Zielgruppe
Ich bin Traumatherapeutin und schreibe ein Buch zum Thema Trauma bearbeiten.
Meine Zielgruppe sucht Heilung, Genesung, Selbstliebe etc.
Aufgabenstellung
Buchcover
Bitte erstell mir ein modernes positives inspirierendes Buchcover mit dem
Titel: 'Morgens LEISE aufbrechen“
Untertitel: „Geh den Pfad, der dich leise ruft“
Dr. Merle Kuhnast
Ich hätte gerne ein modernes Buch, das entweder einen Bezug zum Thema Trauma hat oder aber einfach stylische Schriftzüge. Bin aber auch offen für andere Vorschläge.
Dunkelblau, weiß und türkis oder auch rosa mag ich ganz gerne. Wobei Dunkelblau, weiß und türkis meine Favoriten sind und mit rosa höchstens kleinere Akzente gesetzt werden sollten.
Das Buchcover soll modern sein und direkt ansprechen. Gerne eine originelle Lösung, oder etwas Besonderes, etwas das Tiefe ausdrückt, oder man mehrmals hinsehen muss um etwas zu erkennen oder etwas das mehr Interpretationsspielraum lässt.
Gerne auch viel weiß, zumindest heller und nicht zu dunkel. Stylish, aber nicht überfrachtet.
Schreib mich gerne an, wenn du Fragen hast.
Ich habe mal zwei Beispiel von Typolösungen angehängt, die ich ganz cool fände.
Ich freue mich auf deine Ideen :-)
Ganz liebe Grüße
Merle

```html
<!DOCTYPE html>
<html lang="de">
<head>
<meta charset="utf-8">
<title>Morgens LEISE aufbrechen – Buchcover</title>
<link href="https://fonts.googleapis.com/css2?family=Permanent+Marker&family=Caveat+Brush&family=Montserrat:wght@400;500&display=swap" rel="stylesheet">
<style>
  :root {
    --backdrop: #f1f3f4;
    --teal-deep: #1b6b8c;
    --teal-mid: #1f93a3;
    --turquoise-light: #7af2dc;
    --lime: #b4f01e;
    --ink-white: #f4f4f1;
  }
  html, body {
    margin: 0;
    width: 1200px;
    height: 1200px;
    overflow: hidden;
    background: var(--backdrop);
  }
  .cover {
    position: absolute;
    left: 176px;
    top: 0;
    width: 848px;
    height: 1200px;
    overflow: hidden;
    background:
      radial-gradient(ellipse 70% 55% at 82% 4%, var(--turquoise-light) 0%, rgba(64, 200, 190, 0.85) 30%, rgba(31, 147, 163, 0) 75%),
      linear-gradient(180deg, var(--teal-mid) 0%, #1c8699 55%, var(--teal-deep) 100%);
  }
  .book-title {
    margin: 0;
    font-weight: 400;
  }
  .title-line {
    position: absolute;
    left: 0;
    width: 100%;
    display: block;
    text-align: center;
    font-family: "Permanent Marker", "Caveat Brush", cursive;
    font-weight: 400;
    color: var(--ink-white);
    line-height: 1;
    text-transform: uppercase;
    white-space: nowrap;
  }
  .title-top {
    top: 160px;
    font-size: 88px;
    letter-spacing: 1px;
  }
  .title-main {
    top: 240px;
    font-size: 170px;
    letter-spacing: 2px;
  }
  .title-bottom {
    top: 478px;
    font-size: 82px;
    letter-spacing: 1px;
  }
  .title-underline {
    position: absolute;
    left: 88px;
    top: 440px;
    width: 704px;
    height: 14px;
    border-radius: 7px;
    background: var(--lime);
    transform: rotate(-0.8deg);
  }
  .subtitle {
    position: absolute;
    left: 0;
    width: 100%;
    top: 636px;
    text-align: center;
    font-family: "Montserrat", sans-serif;
    font-weight: 400;
    font-size: 33px;
    line-height: 45px;
    color: var(--ink-white);
    margin: 0;
  }
  .emblem-area {
    position: absolute;
    left: 322px;
    top: 823px;
    width: 204px;
    height: 178px;
    border-radius: 50%;
    background: radial-gradient(circle, rgba(180, 240, 30, 0.35) 0%, rgba(180, 240, 30, 0) 70%);
  }
  .author {
    position: absolute;
    left: 0;
    width: 100%;
    top: 1124px;
    text-align: center;
    font-family: "Montserrat", sans-serif;
    font-weight: 500;
    font-size: 25px;
    color: var(--ink-white);
    margin: 0;
  }
  .footer-bar {
    position: absolute;
    left: 336px;
    top: 1179px;
    width: 177px;
    height: 21px;
    background: var(--lime);
  }
</style>
</head>
<body>
  <main class="cover">
    <h1 class="book-title">
      <span class="title-line title-top">Morgens</span>
      <span class="title-line title-main">Leise</span>
      <span class="title-line title-bottom">aufbrechen</span>
    </h1>
    <div class="title-underline" role="img" aria-label="Platz für die handgezogene grüne Unterstreichung"></div>
    <p class="subtitle">Geh den Pfad,<br>der dich leise ruft</p>
    <div class="emblem-area" role="img" aria-label="Platz für das Schmetterlings-Emblem der Autorin in Limettengrün"></div>
    <p class="author">Dr. Merle Kuhnast</p>
    <div class="footer-bar"></div>
  </main>
</body>
</html>
```